Project Title:
Dental Implant Overdenture Flyer (Retirement Village Target)
Objective:
Create a clean, trustworthy, and reassuring flyer aimed at older adults (60–85 years old) who struggle with loose dentures. The goal is to educate them about implant-retained “clip-on” dentures and encourage them to book a consultation.
Tone & Feel:
Warm, caring, non-intimidating
Premium but not “salesy”
Medical but easy to understand
Focus on improving quality of life (confidence, eating, comfort)
Target Audience:
Retirees / pensioners
Existing denture wearers
People frustrated with loose or uncomfortable dentures
Key Message:
“You don’t have to live with loose dentures anymore.”
Design Style:
Clean, minimal, modern
Soft colours (blues, greens, warm neutrals)
Easy-to-read large font
High contrast for older eyes
Avoid clutter
Imagery Suggestions:
Smiling older adults (natural, not stocky/overly staged)
Before/after lifestyle (eating, laughing, socialising)
Simple diagram showing denture clipping onto implants
Avoid graphic surgical images
Layout Suggestions:
A5 or DL flyer
Clear sections with headings
Icons for benefits
Strong call-to-action at bottom
HEADLINE (big and bold)
Tired of Loose Dentures?
Discover Secure “Clip-On” Teeth
🔹 PROBLEM SECTION
Do your dentures:
Slip or move when eating?
Make it hard to chew certain foods?
Feel uncomfortable or loose?
Affect your confidence when speaking or smiling?
You’re not alone — and there is a better solution.
🔹 SOLUTION SECTION
Implant-Retained “Clip-On” Dentures
We can secure your denture using just 2 dental implants, allowing your teeth to:
✔ Stay firmly in place
✔ Improve your ability to eat
✔ Feel more comfortable
✔ Boost your confidence
🔹 SIMPLE EXPLANATION (very important)
Small titanium implants are gently placed in the jaw.
Your denture then clips securely onto them, stopping movement.
🔹 PRICE SECTION (highlight this clearly)
$12,000
Includes:
2 dental implants
A brand new custom overdenture
Does not include sedation or extractions (if needed)
🔹 SEDATION
Sedation is available for comfort.
If you hold a pensioner card, you may receive a significant Vantrel rebate, often resulting in minimal out-of-pocket costs for sedation.
🔹 TRUST / REASSURANCE
Experienced implant clinician
Gentle, patient-focused care
Modern technology and techniques
🔹 CALL TO ACTION (VERY IMPORTANT)
Book a Free Consultation
📞 Call: 08 5127 3046
🌐 Visit: www.brolvenclinic.com.au
📍 Located near Tallowmere shopping centre
🔹 OPTIONAL TAGLINE
Eat Better. Feel Better. Smile with Confidence Again.
Please include some photos to illustrate what a clip on denture looks like with two implants.

```html
<!DOCTYPE html>
<html lang="en">
<head>
<meta charset="utf-8">
<title>Brolven Clinic – Clip-On Denture Flyer</title>
<link rel="stylesheet" href="https://fonts.googleapis.com/css2?family=Oswald:wght@400;500;600;700&family=Montserrat:wght@500&family=Krona+One&display=swap">
<style>
:root{
  --backdrop:#272727;
  --paper:#f3fcfd;
  --teal:#0a99b6;
  --teal-dark:#08788f;
  --aqua:#20d5cf;
  --ink:#252525;
  --white:#ffffff;
}
*{margin:0;padding:0;box-sizing:border-box}
html,body{width:1200px;height:863px;overflow:hidden;background:var(--backdrop)}
body{position:relative;font-family:"Oswald",sans-serif;color:var(--ink)}
.page{position:absolute;top:111px;width:482px;height:642px;overflow:hidden;
  background:linear-gradient(180deg,var(--paper) 0%,#e9f8fa 100%)}
.page--front{left:108px}
.page--back{left:610px}
.abs{position:absolute}

/* front */
.tagline{left:23px;top:25px;font-family:"Montserrat",sans-serif;font-size:8.5px;font-weight:500}
.brand{left:282px;top:22px;display:flex;align-items:center;gap:7px;font-size:17px;font-weight:500;color:var(--teal);letter-spacing:2px}
.brand__dot{width:12px;height:12px;border-radius:50%;background:var(--aqua)}
.hero-panel{left:0;top:54px;width:255px;height:315px;background:var(--teal);border-radius:0 26px 26px 0}
.hero-disc{left:285px;top:70px;width:300px;height:300px;border-radius:50%;background:var(--aqua)}
.hero-ring{left:212px;top:79px;width:280px;height:280px}
.hero-photo{left:237px;top:103px;width:230px;height:230px;border-radius:50%;border:4px solid var(--white);
  background:radial-gradient(circle at 60% 40%,#e9ddd2 0%,#cdb7a2 55%,#a88f7a 100%)}
.headline{left:26px;top:72px;color:var(--white);font-weight:700;line-height:1}
.headline__small{font-size:37px;display:block}
.headline__big{font-size:66px;display:block;margin:2px 0 0}
.headline__rule{left:26px;top:225px;width:53px;height:2px;background:var(--white)}
.subhead{left:26px;top:238px;color:var(--white);font-weight:600;line-height:1}
.subhead__line{font-size:27px;display:block}
.subhead__clip{font-size:44px;font-weight:700;display:block;margin:6px 0 2px}
.subhead__teeth{font-size:28px;display:block}

.section-title{font-size:24px;font-weight:600;line-height:1.1}
.accent{color:var(--teal)}
.ticks{list-style:none;font-size:12.5px;font-weight:500;white-space:nowrap}
.ticks li{position:relative;padding-left:19px;line-height:19px}
.ticks svg{position:absolute;left:0;top:3px;width:12px;height:12px}
.problem{left:24px;top:384px;width:225px}
.problem .ticks{margin-top:9px}
.reassure{left:26px;top:520px;font-size:17px;font-weight:500;line-height:1.1}
.solution{left:264px;top:382px;width:210px}
.solution__title{font-size:17px;font-weight:500;line-height:1.25}
.solution__title .accent{font-size:22px;font-weight:600}
.solution__lead{font-size:15.5px;font-weight:500;line-height:21px;margin-top:8px}
.solution .ticks{margin-top:4px}

.footer-band{left:0;top:585px;width:482px;height:57px;background:var(--teal)}
.cta{left:26px;top:571px;width:194px;height:29px;border-radius:15px;background:var(--aqua);border:2px solid var(--white);
  color:var(--teal-dark);font-size:16px;font-weight:500;display:flex;align-items:center;justify-content:center;white-space:nowrap}
.phone{left:26px;top:605px;display:flex;align-items:center;gap:8px;color:var(--white);font-family:"Krona One",sans-serif;font-size:21px;white-space:nowrap}
.phone svg{width:17px;height:17px}
.web{left:264px;top:591px;color:var(--white);line-height:1;white-space:nowrap}
.web__row{display:flex;align-items:center;gap:7px}
.web__url{font-size:17px;font-weight:600}
.web__loc{font-size:11px;font-weight:500;margin-top:6px}
.web svg{width:11px;height:11px}

/* back */
.explain{left:0;top:16px;width:482px;text-align:center;font-size:17.5px;font-weight:500;line-height:1.15;white-space:nowrap}
.explain__a{color:var(--teal)}
.price-band{left:0;top:76px;width:482px;height:279px;background:var(--teal)}
.price{left:24px;top:98px;color:var(--white);font-size:66px;font-weight:700;line-height:1;white-space:nowrap}
.includes{left:264px;top:94px;color:var(--white);line-height:1;white-space:nowrap}
.includes__title{font-size:28px;font-weight:600}
.includes__item{font-size:15.5px;font-weight:500;margin-top:9px}
.exclusion{left:24px;top:205px;color:var(--white);font-size:18.5px;font-weight:500;line-height:1.1;white-space:nowrap}
.sedation{left:24px;top:270px;color:var(--white);font-size:21px;font-weight:600;line-height:1.2;white-space:nowrap}
.photo-frame{left:251px;top:205px;width:209px;height:299px;background:var(--white)}
.photo-pair{left:255px;top:209px;width:201px;height:148px;
  background:linear-gradient(90deg,#c9a68c 0%,#e4cdb8 48%,#b7c7d6 52%,#dbc6b3 100%)}
.rebate{left:255px;top:357px;width:201px;height:143px;background:var(--aqua);color:var(--teal-dark);
  font-size:14.5px;font-weight:500;line-height:21px;text-align:center;display:flex;align-items:center;justify-content:center;white-space:nowrap}
.diagram{left:24px;top:386px;width:208px;height:145px;border-radius:40px 40px 60px 60px;
  background:radial-gradient(ellipse at 50% 55%,#f3b7c0 0%,#e99aa8 55%,#f4f4f4 100%)}
.trust{left:259px;top:520px}
</style>
</head>
<body>

<section class="page page--front">
  <p class="abs tagline">Eat Better. Feel Better. Smile with Confidence Again.</p>
  <div class="abs brand"><span class="brand__dot"></span>BROLVEN CLINIC</div>

  <div class="abs hero-disc"></div>
  <svg class="abs hero-ring" viewBox="0 0 280 280" aria-hidden="true">
    <circle cx="140" cy="140" r="128" fill="none" stroke="var(--white)" stroke-width="14"/>
    <path d="M140 12 A128 128 0 0 0 40 218" fill="none" stroke="var(--aqua)" stroke-width="2.5"/>
    <path d="M140 12 A128 128 0 0 1 245 70" fill="none" stroke="var(--teal)" stroke-width="6"/>
    <circle cx="35" cy="75" r="4" fill="var(--aqua)"/>
    <circle cx="12" cy="140" r="5" fill="var(--aqua)"/>
    <circle cx="38" cy="215" r="4" fill="var(--aqua)"/>
  </svg>
  <div class="abs hero-panel"></div>
  <div class="abs hero-photo" role="img" aria-label="Photo of a smiling older woman with short grey hair in a white shirt"></div>

  <h1 class="abs headline">
    <span class="headline__small">TIRED OF</span>
    <span class="headline__big">LOOSE</span>
    <span class="headline__small">DENTURES?</span>
  </h1>
  <div class="abs headline__rule"></div>
  <p class="abs subhead">
    <span class="subhead__line">Discover Secure</span>
    <span class="subhead__clip">“CLIP-ON”</span>
    <span class="subhead__teeth">Teeth</span>
  </p>

  <div class="abs problem">
    <h2 class="section-title">Do your <span class="accent">dentures:</span></h2>
    <ul class="ticks">
      <li><svg viewBox="0 0 12 12"><circle cx="6" cy="6" r="6" fill="var(--aqua)"/><path d="M3.3 6.2l1.8 1.8 3.6-3.7" fill="none" stroke="#fff" stroke-width="1.4"/></svg>Slip or move when eating?</li>
      <li><svg viewBox="0 0 12 12"><circle cx="6" cy="6" r="6" fill="var(--aqua)"/><path d="M3.3 6.2l1.8 1.8 3.6-3.7" fill="none" stroke="#fff" stroke-width="1.4"/></svg>Make it hard to chew certain foods?</li>
      <li><svg viewBox="0 0 12 12"><circle cx="6" cy="6" r="6" fill="var(--aqua)"/><path d="M3.3 6.2l1.8 1.8 3.6-3.7" fill="none" stroke="#fff" stroke-width="1.4"/></svg>Feel uncomfortable or loose?</li>
      <li><svg viewBox="0 0 12 12"><circle cx="6" cy="6" r="6" fill="var(--aqua)"/><path d="M3.3 6.2l1.8 1.8 3.6-3.7" fill="none" stroke="#fff" stroke-width="1.4"/></svg>Affect your confidence when<br>speaking or smiling?</li>
    </ul>
  </div>
  <p class="abs reassure"><span class="accent">You’re not alone – and there is a</span><br>better solution.</p>

  <div class="abs solution">
    <h2 class="solution__title">Implant-Retained <span class="accent">“Clip-On”</span><br>Dentures</h2>
    <p class="solution__lead">We can secure your denture using <span class="accent">just 2 dental implants, allowing your teeth to:</span></p>
    <ul class="ticks">
      <li><svg viewBox="0 0 12 12"><circle cx="6" cy="6" r="6" fill="var(--aqua)"/><path d="M3.3 6.2l1.8 1.8 3.6-3.7" fill="none" stroke="#fff" stroke-width="1.4"/></svg>Stay firmly in place</li>
      <li><svg viewBox="0 0 12 12"><circle cx="6" cy="6" r="6" fill="var(--aqua)"/><path d="M3.3 6.2l1.8 1.8 3.6-3.7" fill="none" stroke="#fff" stroke-width="1.4"/></svg>Improve your ability to eat</li>
      <li><svg viewBox="0 0 12 12"><circle cx="6" cy="6" r="6" fill="var(--aqua)"/><path d="M3.3 6.2l1.8 1.8 3.6-3.7" fill="none" stroke="#fff" stroke-width="1.4"/></svg>Feel more comfortable</li>
      <li><svg viewBox="0 0 12 12"><circle cx="6" cy="6" r="6" fill="var(--aqua)"/><path d="M3.3 6.2l1.8 1.8 3.6-3.7" fill="none" stroke="#fff" stroke-width="1.4"/></svg>Boost your confidence</li>
    </ul>
  </div>

  <div class="abs footer-band"></div>
  <div class="abs cta">Book a Free Consultation</div>
  <p class="abs phone"><svg viewBox="0 0 24 24"><path d="M6.6 10.8a15.1 15.1 0 0 0 6.6 6.6l2.2-2.2c.3-.3.7-.4 1-.2 1.1.4 2.3.6 3.6.6.6 0 1 .4 1 1V20c0 .6-.4 1-1 1A17 17 0 0 1 3 4c0-.6.4-1 1-1h3.5c.6 0 1 .4 1 1 0 1.3.2 2.5.6 3.6.1.3 0 .7-.2 1z" fill="#fff"/></svg>08 5127 3046</p>
  <div class="abs web">
    <p class="web__row web__url"><svg viewBox="0 0 12 12"><circle cx="6" cy="6" r="5" fill="none" stroke="#fff"/><path d="M1 6h10M6 1c-2.5 3-2.5 7 0 10M6 1c2.5 3 2.5 7 0 10" fill="none" stroke="#fff" stroke-width=".8"/></svg>www.brolvenclinic.com.au</p>
    <p class="web__row web__loc"><svg viewBox="0 0 12 12"><path d="M6 11S2 7 2 4.5a4 4 0 0 1 8 0C10 7 6 11 6 11z" fill="#fff"/><circle cx="6" cy="4.5" r="1.5" fill="var(--teal)"/></svg>Located near Tallowmere shopping centre</p>
  </div>
</section>

<section class="page page--back">
  <p class="abs explain"><span class="explain__a">Small titanium implants are gently placed in the jaw.</span><br>Your denture then clips securely onto them, stopping movement.</p>
  <div class="abs price-band"></div>
  <p class="abs price">$12,000</p>
  <div class="abs includes">
    <p class="includes__title">Includes:</p>
    <p class="includes__item">2 dental implants</p>
    <p class="includes__item">A brand new custom overdenture</p>
  </div>
  <p class="abs exclusion">Does not include sedation or<br>extractions (if needed)</p>
  <p class="abs sedation">SEDATION IS AVAILABLE<br>FOR COMFORT.</p>

  <div class="abs photo-frame"></div>
  <div class="abs photo-pair" role="img" aria-label="Before and after photos of an older woman smiling with loose dentures and then with new clip-on dentures"></div>
  <p class="abs rebate">If you hold a pensioner card,<br>you may receive a significant<br>Vantrel rebate, often<br>resulting in minimal<br>out-of-pocket costs for<br>sedation.</p>

  <div class="abs diagram" role="img" aria-label="Illustration of a lower denture clipping onto two titanium implants in the jaw"></div>

  <ul class="abs ticks trust">
    <li><svg viewBox="0 0 12 12"><circle cx="6" cy="6" r="6" fill="var(--aqua)"/><path d="M3.3 6.2l1.8 1.8 3.6-3.7" fill="none" stroke="#fff" stroke-width="1.4"/></svg>Experienced implant clinician</li>
    <li><svg viewBox="0 0 12 12"><circle cx="6" cy="6" r="6" fill="var(--aqua)"/><path d="M3.3 6.2l1.8 1.8 3.6-3.7" fill="none" stroke="#fff" stroke-width="1.4"/></svg>Gentle, patient-focused care</li>
    <li><svg viewBox="0 0 12 12"><circle cx="6" cy="6" r="6" fill="var(--aqua)"/><path d="M3.3 6.2l1.8 1.8 3.6-3.7" fill="none" stroke="#fff" stroke-width="1.4"/></svg>Modern technology and techniques</li>
  </ul>

  <div class="abs footer-band"></div>
  <div class="abs cta">Book a Free Consultation</div>
  <p class="abs phone"><svg viewBox="0 0 24 24"><path d="M6.6 10.8a15.1 15.1 0 0 0 6.6 6.6l2.2-2.2c.3-.3.7-.4 1-.2 1.1.4 2.3.6 3.6.6.6 0 1 .4 1 1V20c0 .6-.4 1-1 1A17 17 0 0 1 3 4c0-.6.4-1 1-1h3.5c.6 0 1 .4 1 1 0 1.3.2 2.5.6 3.6.1.3 0 .7-.2 1z" fill="#fff"/></svg>08 5127 3046</p>
  <div class="abs web">
    <p class="web__row web__url"><svg viewBox="0 0 12 12"><circle cx="6" cy="6" r="5" fill="none" stroke="#fff"/><path d="M1 6h10M6 1c-2.5 3-2.5 7 0 10M6 1c2.5 3 2.5 7 0 10" fill="none" stroke="#fff" stroke-width=".8"/></svg>www.brolvenclinic.com.au</p>
    <p class="web__row web__loc"><svg viewBox="0 0 12 12"><path d="M6 11S2 7 2 4.5a4 4 0 0 1 8 0C10 7 6 11 6 11z" fill="#fff"/><circle cx="6" cy="4.5" r="1.5" fill="var(--teal)"/></svg>Located near Tallowmere shopping centre</p>
  </div>
</section>

</body>
</html>
```